Stationary/Web Page
Project: Business Cards
Business Cards
Professional
Joel Varrick
President
4817 W. Pelham Ridge Dunmore Rd. Baytown, TX 77409
JoelVarrick_OTW@mailbrook.com

```html
<!DOCTYPE html>
<html lang="en">
<head>
<meta charset="utf-8">
<title>Oakline Trade Works – Stationery Set</title>
<link href="https://fonts.googleapis.com/css2?family=Arimo:wght@400;700&display=swap" rel="stylesheet">
<style>
  :root {
    --bg: #1b1b1b;
    --paper: #ffffff;
    --red: #c8101e;
    --red-dark: #7d0a12;
    --ink: #222222;
    --muted: #666666;
  }
  * { margin: 0; padding: 0; box-sizing: border-box; }
  html, body { width: 1200px; height: 899px; overflow: hidden; background: var(--bg); font-family: "Arimo", Arial, sans-serif; color: var(--ink); }
  .canvas { position: relative; width: 1200px; height: 899px; }

  .sheet { position: absolute; background: var(--paper); overflow: hidden; box-shadow: 0 4px 14px rgba(0,0,0,.5); }
  .swoosh { position: absolute; left: 0; bottom: 0; width: 100%; display: block; }

  .brand { display: flex; align-items: center; gap: 7px; }
  .brand-dot { width: 26px; height: 26px; border-radius: 50%; background: var(--red); flex: none; }
  .brand-name { font-weight: 700; color: var(--red); font-size: 15px; letter-spacing: .2px; line-height: 1.1; }
  address { font-style: normal; }

  /* Letterhead */
  .letterhead { left: 61px; top: 85px; width: 394px; height: 693px; }
  .letterhead .brand { position: absolute; left: 22px; top: 26px; }
  .letterhead .brand-name { font-size: 13px; }
  .sender { position: absolute; left: 262px; top: 22px; font-size: 6.5px; line-height: 1.45; color: var(--muted); width: 118px; }
  .letter { position: absolute; left: 22px; top: 118px; width: 350px; font-size: 7px; line-height: 1.55; color: var(--muted); }
  .letter p { margin-bottom: 11px; }
  .recipient { margin-bottom: 12px; }

  /* Business card */
  .card { left: 612px; top: 380px; width: 270px; height: 205px; border-radius: 10px; }
  .card-name { position: absolute; left: 18px; top: 48px; color: #fff; font-weight: 700; font-size: 15px; }
  .card-title { position: absolute; left: 18px; top: 68px; color: #fff; font-size: 7px; }
  .card .brand { position: absolute; left: 140px; top: 94px; }
  .card .brand-dot { width: 18px; height: 18px; }
  .card .brand-name { font-size: 10.5px; }
  .card-contact { position: absolute; left: 18px; top: 140px; font-size: 6.5px; line-height: 1.5; color: var(--muted); }

  /* Envelope */
  .envelope { left: 598px; top: 600px; width: 544px; height: 175px; }
  .envelope .brand { position: absolute; left: 22px; top: 20px; }
  .envelope .brand-dot { width: 22px; height: 22px; }
  .envelope .brand-name { font-size: 13px; }
  .return-address { position: absolute; left: 22px; top: 52px; font-size: 6.5px; line-height: 1.5; color: var(--muted); }
</style>
</head>
<body>
<main class="canvas">

  <section class="sheet letterhead" aria-label="Letterhead">
    <div class="brand"><span class="brand-dot"></span><span class="brand-name">OAKLINE TRADE<br>WORKS LLC</span></div>
    <address class="sender">
      Main Office<br>
      4817 W. Pelham Ridge Dunmore Rd.<br>
      Baytown, TX 77409<br>
      P (555) 014-2290<br>
      F (555) 014-2291<br>
      E JoelVarrick_OTW@mailbrook.com
    </address>
    <div class="letter">
      <p class="recipient">Client Name<br>120 Main St.<br>Harlow, Texas</p>
      <p>Dear Client Name,</p>
      <p>Thank you for meeting with our team last week. We have reviewed your floor plans and prepared a detailed proposal for the new office interiors, including finishes, lighting and furniture layouts for each level.</p>
      <p>Our crews can begin work within two weeks of approval. We will coordinate closely with your building manager to keep noise and disruption low during business hours.</p>
      <p>Please review the enclosed schedule and budget summary. If any item needs adjustment, we are glad to revise the plan and meet again at your convenience.</p>
      <p>We look forward to working with you on this project and to delivering a space your staff will enjoy every day.</p>
      <p>Yours Sincerely,<br>Joel Varrick</p>
    </div>
    <svg class="swoosh" viewBox="0 0 394 150" height="150" aria-hidden="true">
      <path d="M0 62 C130 40 270 22 394 6" fill="none" stroke="#111" stroke-width="3"/>
      <path d="M0 78 C130 52 270 32 394 16 L394 150 L0 150 Z" fill="var(--red)"/>
      <path d="M0 130 C150 110 280 90 394 70 L394 150 L0 150 Z" fill="var(--red-dark)" opacity=".45"/>
      <circle cx="348" cy="108" r="30" fill="#fff"/>
      <circle cx="348" cy="108" r="21" fill="var(--red)"/>
    </svg>
  </section>

  <section class="sheet card" aria-label="Business card">
    <svg class="swoosh" viewBox="0 0 270 205" height="205" style="top:0;bottom:auto" aria-hidden="true">
      <path d="M0 0 H270 V30 C200 40 120 70 0 120 Z" fill="var(--red)"/>
      <path d="M0 126 C120 76 200 46 270 36" fill="none" stroke="#111" stroke-width="2.5"/>
    </svg>
    <div class="card-name">Joel Varrick</div>
    <div class="card-title">President</div>
    <div class="brand"><span class="brand-dot"></span><span class="brand-name">OAKLINE TRADE<br>WORKS LLC</span></div>
    <address class="card-contact">
      4817 W. Pelham Ridge Dunmore Rd.<br>
      Baytown, TX 77409<br>
      P (555) 014-2290<br>
      F (555) 014-2291<br>
      JoelVarrick_OTW@mailbrook.com
    </address>
  </section>

  <section class="sheet envelope" aria-label="Envelope">
    <div class="brand"><span class="brand-dot"></span><span class="brand-name">OAKLINE TRADE<br>WORKS LLC</span></div>
    <address class="return-address">
      Main Office<br>
      4817 W. Pelham Ridge Dunmore Rd.<br>
      Baytown, TX 77409
    </address>
    <svg class="swoosh" viewBox="0 0 544 100" height="100" preserveAspectRatio="none" aria-hidden="true">
      <path d="M0 70 C200 55 380 30 544 8" fill="none" stroke="#111" stroke-width="3"/>
      <path d="M0 82 C200 64 380 40 544 18 L544 100 L0 100 Z" fill="var(--red)"/>
    </svg>
    <svg style="position:absolute;right:12px;bottom:8px" width="64" height="64" viewBox="0 0 64 64" aria-hidden="true">
      <circle cx="32" cy="32" r="30" fill="#fff"/>
      <circle cx="32" cy="32" r="21" fill="var(--red)"/>
    </svg>
  </section>

</main>
</body>
</html>
```